Copperfield Roofing Co. business card design

I am a Roofing contractor in Texas. The name of my company is Copperfield Roofing Co. I also offer a few other services (Christmas light installation, gutters, fencing, pressure washing). However my main gig is roofing. Storm restoration and knowledge of the insurance claim process is my specialty.

My colors are black, red and white. I’d like something pretty simple and clean. Modern looking but with a splash of this red tartan pattern.

I have another version of my logo being edited at the moment where the little top part of the F in roofing that’s currently tartan will be changed to just solid red to make it more visible. So if that’s something you can change in your mock up great. But I can provide the full version once the contest is complete

Target Market(s)

Homeowners

Industry/Entity Type

Roofing

Contact Information for Business Card

Derek Pruitt. 682-555-0193. www.copperfield roofing.co Derek@copperfieldroofing.co

Colors
EB3D1F
EC4F4E
F09395
F8D3D4
FCEDEE

Requirements
Nice to have
• Maybe instead of a business address. I could say serving all DFW Texas or something like that. And maybe add a line somewhere saying deductible assistance? Just a thought

```html
<!DOCTYPE html>
<html lang="en">
<head>
<meta charset="utf-8">
<title>Copperfield Roofing Co. — Business Card</title>
<link rel="stylesheet" href="https://fonts.googleapis.com/css2?family=Montserrat:wght@400;500;700;800&display=swap">
<style>
  :root {
    --stage: #c4c4c4;
    --card: #232323;
    --red: #d42a2a;
    --red-bright: #eb3d1f;
    --white: #ffffff;
    --muted: #e6e6e6;
    --divider: #5a1f1f;
  }
  * { box-sizing: border-box; margin: 0; padding: 0; }
  html, body {
    width: 1200px;
    height: 802px;
    overflow: hidden;
  }
  body {
    background: linear-gradient(180deg, #d2d2d2 0%, #a9a9a9 100%);
    font-family: "Montserrat", sans-serif;
    display: flex;
    align-items: center;
    justify-content: center;
    gap: 40px;
  }
  .card {
    position: relative;
    width: 540px;
    height: 309px;
    background: var(--card);
    border-bottom: 4px solid var(--red);
    box-shadow: 0 14px 30px rgba(0,0,0,0.35);
    overflow: hidden;
  }

  /* Contact side */
  .brand {
    position: absolute;
    left: 42px;
    top: 44px;
    display: flex;
    align-items: center;
    gap: 14px;
  }
  .brand-dot {
    width: 46px;
    height: 46px;
    border-radius: 50%;
    background: var(--red);
    flex: none;
  }
  .brand-name {
    font-weight: 800;
    font-size: 19px;
    line-height: 1.15;
    letter-spacing: 0.5px;
    text-transform: uppercase;
    color: var(--red);
  }
  .person {
    position: absolute;
    left: 42px;
    bottom: 56px;
  }
  .person-name {
    font-weight: 800;
    font-size: 24px;
    letter-spacing: 1px;
    text-transform: uppercase;
    color: var(--red);
  }
  .person-role {
    margin-top: 4px;
    font-weight: 500;
    font-size: 14px;
    color: var(--white);
  }
  .divider {
    position: absolute;
    left: 274px;
    top: 150px;
    width: 1px;
    height: 90px;
    background: var(--divider);
  }
  .contacts {
    position: absolute;
    left: 296px;
    top: 150px;
    list-style: none;
    display: flex;
    flex-direction: column;
    gap: 14px;
  }
  .contacts li {
    display: flex;
    align-items: center;
    gap: 9px;
    font-size: 12px;
    font-weight: 400;
    color: var(--muted);
    white-space: nowrap;
  }
  .contacts svg { width: 11px; height: 11px; flex: none; }

  /* Brand side */
  .front-mark {
    position: absolute;
    right: 40px;
    top: 120px;
    text-align: right;
  }
  .front-mark .brand-row {
    display: flex;
    align-items: center;
    justify-content: flex-end;
    gap: 16px;
  }
  .front-mark .brand-dot { width: 58px; height: 58px; }
  .front-mark .brand-name { font-size: 28px; }
  .tagline {
    margin-top: 14px;
    font-weight: 500;
    font-size: 15px;
    color: var(--white);
  }
</style>
</head>
<body>

  <section class="card card-contact" aria-label="Business card, contact side">
    <div class="brand">
      <span class="brand-dot" aria-hidden="true"></span>
      <p class="brand-name">Copperfield<br>Roofing Co.</p>
    </div>

    <div class="person">
      <p class="person-name">Derek Pruitt</p>
      <p class="person-role">CEO/Founder</p>
    </div>

    <span class="divider" aria-hidden="true"></span>

    <ul class="contacts">
      <li>
        <svg viewBox="0 0 12 12" aria-hidden="true"><path fill="#d42a2a" d="M2.3 1l1.9-.1.9 2.4-1.2.9a6.5 6.5 0 0 0 3 3l.9-1.2 2.4.9-.1 1.9c-.1.6-.6 1-1.2 1A9.2 9.2 0 0 1 1.3 2.2c0-.6.4-1.1 1-1.2z"/></svg>
        682-555-0193
      </li>
      <li>
        <svg viewBox="0 0 12 12" aria-hidden="true"><rect x="0.5" y="2" width="11" height="8" rx="1" fill="#d42a2a"/><path d="M1 2.5l5 4 5-4" fill="none" stroke="#232323" stroke-width="1"/></svg>
        Derek@copperfieldroofing.co
      </li>
      <li>
        <svg viewBox="0 0 12 12" aria-hidden="true"><circle cx="6" cy="6" r="5.5" fill="#d42a2a"/><path d="M0.5 6h11M6 0.5c-2.6 3-2.6 8 0 11M6 0.5c2.6 3 2.6 8 0 11" fill="none" stroke="#232323" stroke-width="0.8"/></svg>
        www.copperfield roofing.co
      </li>
    </ul>
  </section>

  <section class="card card-brand" aria-label="Business card, brand side">
    <div class="front-mark">
      <div class="brand-row">
        <span class="brand-dot" aria-hidden="true"></span>
        <p class="brand-name">Copperfield<br>Roofing Co.</p>
      </div>
      <p class="tagline">Serving all DFW Texas</p>
    </div>
  </section>

</body>
</html>
```